R T Aesthetics

I would like a double sided A5 sized flyer created with a Bold, Playful, Design. The company will be providing Velunex services. We have facebook and instagam accounts set up along with a phone number, would be good to have them along the book of the back page. Simplistic design on the front, would be great to come up with a company logo that compliments the fresh look of the flyer. The back side would be for a list of services provided. I have attached a picture of an example. However other creative ideas would be of interest. Many thanks.

• It would be be good to have a box or some sort on the back page advertising "£30 off first visit" and "30% off you both when you refer a friend"
• Would be good to have a stock picture of on the front of a model of some sort etc.

```html
<!DOCTYPE html>
<html lang="en">
<head>
<meta charset="utf-8">
<title>R T Aesthetics – A5 Flyer</title>
<link href="https://fonts.googleapis.com/css2?family=Cinzel:wght@400;600;700&family=Crimson+Text:wght@400;600;700&display=swap" rel="stylesheet">
<style>
  :root{
    --stage:#e4e4e4;
    --blush:#f1dfdc;
    --blush-light:#f7ecea;
    --blush-deep:#e9d1cd;
    --steel:#7d97a6;
    --steel-dark:#6f8b9b;
    --taupe:#b8a5a1;
    --ink:#1f1f1f;
    --text:#3d3a3a;
    --row-grey:#dedcdc;
    --row-pink:#ecd7d4;
    --white:#ffffff;
    --skin-a:#f2d8cc;
    --skin-b:#d9b3a3;
    --hair:#4a3a35;
  }
  *{box-sizing:border-box;margin:0;padding:0}
  html,body{width:674px;height:1200px;overflow:hidden;background:var(--stage)}
  body{position:relative;font-family:"Crimson Text",Georgia,serif;color:var(--text)}
  .page{position:absolute;left:137px;width:400px;height:566px;overflow:hidden;
    background:linear-gradient(170deg,var(--blush-deep) 0%,var(--blush-light) 45%,var(--blush) 100%);
    box-shadow:0 2px 8px rgba(0,0,0,.12)}
  .page--front{top:23px}
  .page--back{top:611px}

  /* shared */
  .brand{position:absolute;display:flex;align-items:center;gap:6px}
  .brand__dot{width:22px;height:22px;border-radius:50%;background:var(--blush-deep)}
  .brand__name{font-family:"Cinzel",Georgia,serif;font-weight:600;color:var(--steel);font-size:17px;letter-spacing:1px}
  .welcome{position:absolute;font-family:"Crimson Text",Georgia,serif;font-size:8px;letter-spacing:.6px;color:var(--ink);text-transform:uppercase}
  .call-band{position:absolute;font-family:"Cinzel",Georgia,serif;font-weight:700;color:var(--ink);display:flex;align-items:center;background:var(--taupe)}
  .footer{position:absolute;left:0;bottom:0;width:100%;height:26px;background:var(--steel);display:flex;align-items:center;justify-content:center;gap:8px;color:var(--white);font-size:7px;letter-spacing:1px}
  .footer__sep{opacity:.7}
  .social{display:flex;gap:3px}
  .social__dot{width:7px;height:7px;border-radius:50%;background:var(--white)}

  /* front */
  .front-photo{position:absolute;left:0;top:0;width:235px;height:540px;
    background:radial-gradient(ellipse at 60% 40%,var(--skin-a) 0%,var(--skin-b) 60%,var(--hair) 100%);
    border-radius:0 60% 45% 0 / 0 40% 55% 0;opacity:.9}
  .front .brand{left:262px;top:118px}
  .front .welcome{left:246px;top:185px;width:154px;text-align:center}
  .headline{position:absolute;left:216px;top:247px;width:184px;text-align:center;font-family:"Cinzel",Georgia,serif;color:var(--ink)}
  .headline__small{display:block;font-size:17px;line-height:20px}
  .headline__big{display:block;font-size:27px;line-height:30px;color:var(--steel)}
  .rule{position:absolute;left:228px;top:335px;width:136px;height:1px;background:var(--steel)}
  .rule::after{content:"";position:absolute;left:60px;top:-1px;width:16px;height:3px;background:var(--steel)}
  .tagline{position:absolute;left:216px;top:341px;width:184px;text-align:center;font-size:7px;line-height:9px;color:var(--ink)}
  .front .call-band{left:69px;top:506px;width:262px;height:34px;border-radius:12px 12px 0 0;justify-content:center;font-size:18px;letter-spacing:.5px}

  /* back */
  .back .brand{left:50%;transform:translateX(-50%);top:40px}
  .back .welcome{left:0;top:90px;width:100%;text-align:center}
  .section-pill{position:absolute;left:150px;top:107px;width:100px;height:18px;border-radius:9px;background:var(--taupe);font-family:"Cinzel",Georgia,serif;font-size:11px;color:var(--ink);text-align:center;line-height:18px;letter-spacing:.5px}
  .back .subtitle{position:absolute;top:131px;width:100%;text-align:center;font-size:7px;letter-spacing:.5px;color:var(--ink)}
  .price-list{position:absolute;left:49px;top:148px;width:302px;border-collapse:separate;border-spacing:0 4px;font-size:8px;color:var(--ink)}
  .price-list td{height:16px;padding:0 14px}
  .price-list .treatment{background:var(--row-grey)}
  .price-list .price{width:108px;font-weight:700;background:var(--row-pink)}
  .price-list tr:nth-child(even) .treatment{background:var(--row-pink)}
  .price-list tr:nth-child(even) .price{background:var(--row-grey)}
  .about{position:absolute;top:302px;width:150px;font-size:5px;line-height:6.5px;color:var(--text)}
  .about--left{left:49px}
  .about--right{left:225px}
  .about__title{font-size:6.5px;line-height:7.5px;letter-spacing:.3px;text-transform:uppercase;color:var(--ink);margin-bottom:2px}
  .offer{position:absolute;left:52px;width:230px;height:36px;border-radius:14px 0 0 14px;background:var(--steel);display:flex;align-items:center;gap:6px;padding-left:14px;color:var(--white)}
  .offer--first{top:394px}
  .offer--refer{top:442px;background:var(--steel-dark)}
  .offer__amount{font-family:"Crimson Text",Georgia,serif;font-size:27px;font-weight:600;line-height:1}
  .offer__off{font-size:5px;align-self:flex-start;margin-top:9px;margin-left:-5px}
  .offer__text{font-family:"Cinzel",Georgia,serif;font-weight:700;font-size:8.5px;line-height:10px;letter-spacing:.4px}
  .back-photo{position:absolute;left:258px;top:356px;width:142px;height:210px;
    background:radial-gradient(ellipse at 45% 45%,var(--skin-a) 0%,var(--skin-b) 65%,var(--blush) 100%)}
  .back .call-band{left:0;top:512px;width:270px;height:28px;border-radius:0 14px 0 0;padding-left:30px;font-weight:600;font-size:12px;color:var(--white)}
</style>
</head>
<body>

<section class="page page--front front" aria-label="Flyer front">
  <div class="front-photo" role="img" aria-label="Portrait of a model receiving a facial injection from a gloved hand"></div>
  <div class="brand"><span class="brand__dot"></span><span class="brand__name">R T</span></div>
  <p class="welcome">Welcome to R T Aesthetics</p>
  <h1 class="headline">
    <span class="headline__small">Fell More</span>
    <span class="headline__big">Beautiful</span>
    <span class="headline__small">Than Ever</span>
  </h1>
  <div class="rule"></div>
  <p class="tagline">I believe beauty is so much more than skin deep:<br>our skin reflects our inner health and happiness.</p>
  <div class="call-band">CALL US&nbsp; 07700900123</div>
  <footer class="footer">
    <span>www.rtfacialaesthetics.com</span><span class="footer__sep">|</span>
    <span class="social"><span class="social__dot"></span><span class="social__dot"></span></span>
  </footer>
</section>

<section class="page page--back back" aria-label="Flyer back">
  <div class="brand"><span class="brand__dot"></span><span class="brand__name">R T</span></div>
  <p class="welcome">Welcome to R T Aesthetics</p>
  <h2 class="section-pill">TREATMENTS</h2>
  <p class="subtitle">NMC REGISTERED NURSE</p>
  <table class="price-list">
    <tr><td class="treatment">Skin/ Treatment consultation</td><td class="price">£20</td></tr>
    <tr><td class="treatment">Dermaplanning</td><td class="price">From £40</td></tr>
    <tr><td class="treatment">Bespoke Dermaveil Facials</td><td class="price">£70</td></tr>
    <tr><td class="treatment">Collagen Induction Therapy</td><td class="price">From £150</td></tr>
    <tr><td class="treatment">Skin Peels</td><td class="price">From £70</td></tr>
    <tr><td class="treatment">Lumira LED Light Therapy</td><td class="price">£45 per session</td></tr>
    <tr><td class="treatment">Wrinkle Relaxing Treatments</td><td class="price">From £170</td></tr>
  </table>
  <div class="about about--left">
    <p class="about__title">How I am<br>a NMC registered nurse</p>
    <p>Every treatment begins with a careful consultation and a plan built around your skin. I trained in clinical nursing and bring that same care, safety and attention to detail to each visit.</p>
  </div>
  <div class="about about--right">
    <p class="about__title">How I am<br>a NMC registered nurse</p>
    <p>Results should look natural and feel like you. I work gently, explain every step and follow up after each appointment so you always feel supported from start to finish.</p>
  </div>
  <div class="offer offer--first"><span class="offer__amount">£30</span><span class="offer__off">OFF</span><span class="offer__text">FIRST VISIT</span></div>
  <div class="offer offer--refer"><span class="offer__amount">30%</span><span class="offer__off">OFF</span><span class="offer__text">YOU BOTH WHEN<br>YOU REFER A FRIEND</span></div>
  <div class="back-photo" role="img" aria-label="Model receiving a treatment from blue-gloved hands"></div>
  <div class="call-band">CALL US 07700900123</div>
  <footer class="footer">
    <span>www.rtfacialaesthetics.com</span><span class="footer__sep">|</span>
    <span class="social"><span class="social__dot"></span><span class="social__dot"></span></span>
  </footer>
</section>

</body>
</html>
```